KLV Messaging - veteran and exclusive boutique copywriting agency

PROJECT NEEDS:
1. Website design - full homepage design and inner page top banner design
2. Logo design
* Please see attached Briefs (Word Docs) for descriptions of what is needed for 1 and 2 above.
ABOUT THE CLIENT:
KLV Messaging is a veteran and exclusive boutique copywriting agency run by Marcus Holloway. Marcus is an award-winning published novelist and an accomplished executive ghostwriter with articles regularly published prominent technology publications like Brisk, ByteHarbor, FoundryPulse, and more. For nearly three decades, Marcus has focused solely on the technology sector - serving clients in Israel, Europe and the US.

Target Market(s)

hi-tech companies run by serious, confident professionals.

Industry/Entity Type

Business

Number of Pages Required

2 page

Font styles to use
Sans Serif
Other font styles liked:
• font should be modern

Colors
0054AA
0677BA
7BADD7
CADEEF
E8F1F8
F0912C
F2A743
F7CA91
FBE8D2
FDF5EE

Requirements
Must have
• psd files for logo, homepage design, and inner page top banner design
Nice to have
• Please see attached Website and Logo Design Briefs (Word Docs)
Should not have

```html
<!DOCTYPE html>
<html lang="en">
<head>
<meta charset="utf-8">
<title>KLV Messaging — Your Voice, My Words</title>
<link rel="stylesheet" href="https://fonts.googleapis.com/css2?family=Barlow:wght@400;500;600&family=Lexend:wght@400;500;600&family=Poppins:wght@300;400;600;700&display=swap">
<style>
:root{
  --blue-deep:#0054AA;
  --blue:#0677BA;
  --blue-mid:#7BADD7;
  --blue-pale:#CADEEF;
  --blue-mist:#E8F1F8;
  --orange:#F0912C;
  --orange-light:#F2A743;
  --orange-pale:#F7CA91;
  --orange-mist:#FBE8D2;
  --cream:#FDF5EE;
  --ink:#333a45;
  --white:#ffffff;
}
*{margin:0;padding:0;box-sizing:border-box}
html,body{width:1200px;height:3620px;overflow:hidden;background:var(--white)}
body{position:relative;font-family:'Barlow',sans-serif;color:var(--ink)}
.abs{position:absolute}
.heading{font-family:'Lexend',sans-serif;font-weight:600;color:var(--blue-deep);letter-spacing:1px;text-transform:uppercase}
.btn{position:absolute;display:flex;align-items:center;justify-content:center;font-family:'Lexend',sans-serif;font-weight:600;font-size:13px;letter-spacing:.5px;text-transform:uppercase;border-radius:24px}

/* hero */
.hero-bg{position:absolute;left:0;top:0}
.brand{left:140px;top:12px;display:flex;align-items:center;gap:8px;font-family:'Poppins',sans-serif;font-weight:600;color:var(--white)}
.brand-dot{width:18px;height:18px;border-radius:50%;background:var(--orange)}
.brand-name{display:flex;flex-direction:column;line-height:1}
.brand-name .main{font-size:44px;letter-spacing:1px}
.brand-name .sub{font-size:14px;margin-top:2px;letter-spacing:.5px}
.nav{left:341px;top:36px;font-family:'Poppins',sans-serif;font-size:13px;letter-spacing:.6px;color:var(--white)}
.nav span{position:absolute;white-space:nowrap}
.nav-cta{left:954px;top:24px;width:137px;height:40px;background:var(--orange);color:var(--white);border-radius:2px;font-family:'Poppins',sans-serif;font-weight:400;font-size:13px}
.hero-title{left:143px;top:214px;font-family:'Poppins',sans-serif;color:var(--white);font-size:60px;line-height:66px}
.hero-title .light{font-weight:300;position:relative}
.hero-title .bold{font-weight:700;display:block}
.hero-accent{left:372px;top:218px;width:76px;height:76px;border-radius:50%;background:var(--orange)}
.hero-sub{left:143px;top:362px;width:430px;font-family:'Poppins',sans-serif;font-size:18.5px;line-height:30px;color:var(--white)}
.hero-cta{left:150px;top:450px;width:186px;height:51px;border:2px solid var(--white);border-radius:4px;color:var(--white);overflow:hidden}
.hero-cta::after{content:"";position:absolute;right:-14px;bottom:-14px;width:34px;height:34px;border-radius:50%;background:var(--orange)}
.hero-portrait{left:640px;top:84px;width:370px;height:612px;border-radius:180px 180px 0 0;background:linear-gradient(180deg,#9cc4e6 0%,#6ea4d4 55%,#3f6f9c 100%)}

/* client strip */
.clients{left:86px;top:768px;width:1064px;height:105px;border:1.5px solid var(--blue-pale);border-radius:53px}
.client{position:absolute;top:38px;font-family:'Poppins',sans-serif;font-weight:600;font-size:21px;color:#4a5566;display:flex;align-items:center;gap:7px}
.client i{display:block;width:14px;height:14px;border-radius:50%;background:var(--orange)}
.chev{position:absolute;top:40px}

/* what I do */
.section-title{left:0;width:1200px;text-align:center;font-size:33px}
.rule{height:3px;background:var(--orange)}
.intro{left:205px;top:1010px;width:790px;text-align:center;font-size:17px;line-height:29px;color:#444}
.service{position:absolute;top:1156px;width:330px;height:330px;border-radius:50%;background:var(--white);box-shadow:0 6px 30px rgba(6,119,186,.14);text-align:center;padding-top:60px}
.service.featured{background:var(--orange);border:5px solid var(--white);box-shadow:0 0 0 3px var(--orange),0 6px 30px rgba(240,145,44,.25)}
.service h3{font-family:'Lexend',sans-serif;font-weight:600;font-size:17px;color:var(--blue-deep);letter-spacing:.5px;margin-top:20px}
.service h4{font-family:'Poppins',sans-serif;font-weight:600;font-size:11px;color:#222;margin-top:6px}
.service p{font-family:'Poppins',sans-serif;font-size:11px;line-height:15px;color:#444;width:220px;margin:6px auto 0}
.service .more{position:static;display:inline-flex;width:130px;height:34px;background:var(--blue-deep);color:var(--white);font-size:10px;margin-top:16px;border-radius:17px}
.service.featured h3,.service.featured h4,.service.featured p{color:var(--white)}

/* why */
.why{left:0;top:1579px;width:1200px;height:560px;background:var(--blue-deep)}
.why-photo{position:absolute;right:0;top:0;width:627px;height:560px;clip-path:polygon(197px 0,100% 0,100% 100%,0 100%);background:linear-gradient(135deg,#b9b8b4 0%,#d6d4d0 45%,#8d8c88 100%)}
.why-kicker{left:143px;top:1698px;font-family:'Lexend',sans-serif;font-size:12px;letter-spacing:1px;color:var(--white);font-weight:500}
.why-title{left:143px;top:1718px;font-size:30px;color:var(--white)}
.why-text{left:143px;top:1770px;width:420px;font-size:17px;line-height:29px;color:var(--white)}
.why-text p+p{margin-top:15px}
.why-cta{left:143px;top:2010px;width:173px;height:46px;background:var(--orange);color:var(--white)}

/* testimonials */
.kicker{left:0;width:1200px;text-align:center;font-family:'Lexend',sans-serif;font-size:12px;color:var(--orange);letter-spacing:.5px}
.quote{position:absolute;top:2332px;width:447px;height:241px;border:1.5px solid var(--blue-mid);text-align:center;padding:50px 56px 0;font-size:15.5px;line-height:27px;color:#333}
.quote strong{display:block;font-weight:600;font-size:14px;margin-top:2px;color:#111}
.avatar{position:absolute;top:2290px;width:64px;height:64px;border-radius:50%;background:radial-gradient(circle at 50% 40%,#c9a58a,#7a5a44);border:2px solid var(--white)}

/* contact */
.contact-bg{position:absolute;left:0;top:2677px}
.contact-title{left:166px;top:2760px;font-size:32px;color:var(--white)}
.field{position:absolute;left:164px;width:441px;height:44px;background:var(--white);border:1px solid #e6c9a8;font-size:14px;color:#333;padding:14px 18px}
.submit{left:168px;top:3102px;width:174px;height:48px;background:var(--blue-deep);color:var(--white)}
.contact-visual{left:681px;top:2763px;width:414px;height:414px;border-radius:50%;background:radial-gradient(circle at 50% 55%,#4a9be0 0%,#1763c4 55%,#0a3f94 100%)}

/* footer */
.foot-brand{left:198px;top:3338px;font-family:'Poppins',sans-serif;font-weight:600;color:var(--blue-deep);display:flex;flex-direction:column;line-height:1}
.foot-brand .main{font-size:48px;letter-spacing:2px}
.foot-brand .sub{font-size:15px;margin-top:4px;letter-spacing:.5px}
.social{position:absolute;top:3429px;width:28px;height:28px;border-radius:50%;border:1.5px solid var(--orange)}
.social.blue{border-color:var(--blue-deep)}
.foot-col{position:absolute;top:3350px;font-family:'Poppins',sans-serif;font-size:12.5px;color:#333}
.foot-col h5{font-family:'Lexend',sans-serif;font-weight:600;font-size:13.5px;letter-spacing:1px;color:var(--blue-deep);text-transform:uppercase;padding-bottom:8px;border-bottom:1.5px solid var(--blue-pale);width:112px;margin-bottom:14px}
.foot-col li{list-style:none;height:28px}
.contact-row{display:flex;gap:12px;align-items:flex-start;margin-bottom:12px;line-height:17px}
.contact-row svg{flex:none}
.copyright{left:0;top:3580px;width:1200px;text-align:center;font-family:'Poppins',sans-serif;font-size:12px;color:#333}
.copyright u{color:var(--blue-deep)}
.foot-line{left:0;top:3560px;width:1200px;height:1px;background:#dfe6ee}
</style>
</head>
<body>

<!-- HERO -->
<svg class="hero-bg" width="1200" height="740" viewBox="0 0 1200 740" aria-hidden="true">
  <defs>
    <linearGradient id="heroGrad" x1="0" y1="0" x2="1" y2="1">
      <stop offset="0" stop-color="#0a5fb4"/>
      <stop offset="1" stop-color="#0b4ea6"/>
    </linearGradient>
  </defs>
  <path d="M0 505 Q200 680 560 716 Q920 740 1200 462 V488 Q930 760 560 730 Q190 700 0 520 Z" fill="var(--orange)"/>
  <path d="M0 0 H1200 V462 Q920 740 560 716 Q200 680 0 505 Z" fill="url(#heroGrad)"/>
  <circle cx="643" cy="208" r="22" fill="none" stroke="#2f8ad6" stroke-width="4"/>
  <circle cx="62" cy="340" r="20" fill="none" stroke="#2f8ad6" stroke-width="3"/>
</svg>
<div class="abs hero-portrait" role="img" aria-label="Portrait photo of Marcus Holloway in a light blue shirt"></div>

<div class="abs brand"><span class="brand-dot"></span><span class="brand-name"><span class="main">KLV</span><span class="sub">Messaging</span></span></div>
<nav class="abs nav">
  <span style="left:0">ABOUT</span>
  <span style="left:105px">SERVICES</span>
  <span style="left:230px">INDUSTRIES</span>
  <span style="left:368px">PORTFOLIO</span>
  <span style="left:504px">CLIENTS</span>
</nav>
<div class="btn nav-cta">CONTACT ›</div>

<div class="abs hero-accent"></div>
<h1 class="abs hero-title"><span class="light">Your Voice,</span><span class="bold">My Words.</span></h1>
<p class="abs hero-sub">Copywriting and executive ghostwriting that speaks for your vision and your technology.</p>
<div class="btn hero-cta">Contact us ›</div>

<!-- CLIENTS -->
<div class="abs clients">
  <svg class="chev" style="left:44px" width="14" height="24" viewBox="0 0 14 24"><path d="M11 3 3 12l8 9" fill="none" stroke="#777" stroke-width="2"/></svg>
  <div class="client" style="left:88px"><i></i>Arvella</div>
  <div class="client" style="left:262px">Nextrow</div>
  <div class="client" style="left:428px">Quorlo</div>
  <div class="client" style="left:580px"><i style="background:#5aa43a"></i>Tessify</div>
  <div class="client" style="left:722px"><i style="background:var(--blue-deep)"></i>Helixgate</div>
  <div class="client" style="left:890px">Vantrel</div>
  <svg class="chev" style="left:1003px" width="14" height="24" viewBox="0 0 14 24"><path d="M3 3l8 9-8 9" fill="none" stroke="#777" stroke-width="2"/></svg>
</div>

<!-- WHAT I DO -->
<h2 class="abs heading section-title" style="top:943px">What I do</h2>
<div class="abs rule" style="left:567px;top:990px;width:66px"></div>
<p class="abs intro">Based just north of Tel Aviv, KLV Messaging provides messaging, collateral creation, creative, content marketing, and consulting to companies in Israel and abroad. My writing is concise, elegant, and professional - while at the same time reflecting an understated creativity and sense</p>

<div class="service" style="left:136px">
  <svg width="50" height="50" viewBox="0 0 50 50"><g fill="none" stroke="var(--orange)" stroke-width="2"><path d="M18 27a9 9 0 1 1 14 0c-2 2-3 4-3 7h-8c0-3-1-5-3-7z"/><path d="M21 38h8M22 42h6"/><path d="M25 6v4M10 12l3 3M40 12l-3 3M6 24h4M40 24h4"/></g></svg>
  <h3>MESSAGING</h3>
  <h4>The Value of a Fresh Perspective</h4>
  <p>Could you be reaching farther? Clearly-defined, accurately-targeted messaging is crucial.</p>
  <span class="btn more">Learn more</span>
</div>
<div class="service featured" style="left:442px;top:1153px;width:336px;height:336px">
  <svg width="50" height="50" viewBox="0 0 50 50"><g fill="none" stroke="var(--white)" stroke-width="2"><rect x="10" y="8" width="30" height="36"/><path d="M16 16h18M16 22h18M16 28h10M16 34h10"/><rect x="30" y="28" width="6" height="8"/></g></svg>
  <h3>COLLATERAL</h3>
  <h4>Concise, Effective, Creative</h4>
  <p>Marketing collateral that effectively communicates who you are and what you want to say.</p>
  <span class="btn more">Learn more</span>
</div>
<div class="service" style="left:758px">
  <svg width="50" height="50" viewBox="0 0 50 50"><g fill="none" stroke="var(--blue-deep)" stroke-width="2"><rect x="9" y="9" width="32" height="32"/><path d="M9 15h32M14 21h12M14 27h12M14 33h20"/><rect x="29" y="20" width="7" height="8"/></g></svg>
  <h3>CONTENT MARKETING</h3>
  <h4>Giving Voice to Your Vision</h4>
  <p>Articles, blog content, white papers, e-books. Your ideas and expertise, our words.</p>
  <span class="btn more">Learn more</span>
</div>

<!-- WHY CHOOSE ME -->
<section class="abs why">
  <div class="why-photo" role="img" aria-label="Photo of a desktop monitor showing the word copywriting on a desk by a stone wall"></div>
</section>
<div class="abs why-kicker">WHY WE ARE</div>
<h2 class="abs heading why-title">Why choose me</h2>
<div class="abs why-text">
  <p>In a noisy marketplace, the value of clearly-defined, accurately-targeted, and well-conceived company messages is easy to see.</p>
  <p>However, what's clear to you may be less so to others. Are the messages and texts you've been recycling hitting their mark with all prospects? Could you be saying more? Could you be reaching farther?</p>
</div>
<div class="btn why-cta">Learn more ›</div>

<!-- TESTIMONIALS -->
<div class="abs kicker" style="top:2213px">TESTIMONIALS</div>
<h2 class="abs heading section-title" style="top:2226px;font-size:29px">What they're saying</h2>
<div class="abs rule" style="left:577px;top:2265px;width:46px"></div>

<svg class="abs" style="left:88px;top:2410px" width="24" height="44" viewBox="0 0 24 44"><path d="M20 3 4 22l16 19" fill="none" stroke="var(--blue)" stroke-width="2.5"/></svg>
<blockquote class="quote" style="left:144px">“We've been working with Marcus for over three years. He understands our technology and business model - and communicates it succinctly, in a language that our target audience understands and responds to.”<strong>Daniel Orenstein, CTO, Vantrel</strong></blockquote>
<blockquote class="quote" style="left:613px">“We've been working with Marcus for over three years. He understands our technology and business model - and communicates it succinctly, in a language that our target audience understands and responds to.”<strong>Daniel Orenstein, CTO, Vantrel</strong></blockquote>
<div class="avatar" style="left:335px" role="img" aria-label="Client headshot"></div>
<div class="avatar" style="left:798px;background:radial-gradient(circle at 50% 40%,#8a6248,#3e2a20)" role="img" aria-label="Client headshot"></div>
<svg class="abs" style="left:1094px;top:2410px" width="24" height="44" viewBox="0 0 24 44"><path d="M4 3l16 19L4 41" fill="none" stroke="var(--blue)" stroke-width="2.5"/></svg>

<!-- CONTACT -->
<svg class="contact-bg" width="1200" height="620" viewBox="0 0 1200 620" aria-hidden="true">
  <defs>
    <linearGradient id="contactGrad" x1="0" y1="0" x2="1" y2="1">
      <stop offset="0" stop-color="var(--orange-light)"/>
      <stop offset="1" stop-color="var(--orange)"/>
    </linearGradient>
  </defs>
  <path d="M0 470 Q360 650 1200 480 V520 Q400 690 0 490 Z" fill="var(--blue-deep)"/>
  <path d="M0 0 H1200 V478 Q420 640 0 470 Z" fill="url(#contactGrad)"/>
  <path d="M160 134 Q220 128 284 132" fill="none" stroke="var(--white)" stroke-width="4" stroke-linecap="round"/>
  <circle cx="888" cy="293" r="226" fill="none" stroke="var(--white)" stroke-width="1.5" opacity=".8"/>
  <circle cx="888" cy="293" r="240" fill="none" stroke="var(--white)" stroke-width="1" opacity=".6"/>
</svg>
<h2 class="abs heading contact-title">Contact us</h2>
<div class="field" style="top:2835px">Your Name*</div>
<div class="field" style="top:2890px">E-mail address*</div>
<div class="field" style="top:2945px">Phone*</div>
<div class="field" style="top:3000px;height:84px">Message</div>
<div class="btn submit">Submit ›</div>
<div class="abs contact-visual" role="img" aria-label="Illustration of hands typing on a laptop with blue business charts"></div>

<!-- FOOTER -->
<div class="abs foot-brand"><span class="main">KLV</span><span class="sub">Messaging</span></div>
<span class="social" style="left:199px" aria-label="Social profile"></span>
<span class="social blue" style="left:233px" aria-label="Social profile"></span>
<span class="social blue" style="left:268px" aria-label="Social profile"></span>
<span class="social blue" style="left:303px" aria-label="Social profile"></span>

<div class="foot-col" style="left:466px">
  <h5>Navigation</h5>
  <ul><li>About</li><li>Services</li><li>Industries</li><li>Portfolio</li><li>Clients</li></ul>
</div>
<div class="foot-col" style="left:667px">
  <h5>Resources</h5>
  <ul><li>Privacy Policy</li><li>Terms of Use</li><li>Sitemap</li><li>Contact Us</li></ul>
</div>
<div class="foot-col" style="left:881px">
  <h5>Contact us</h5>
  <div class="contact-row">
    <svg width="28" height="28" viewBox="0 0 28 28"><circle cx="14" cy="14" r="14" fill="var(--blue-deep)"/><path d="M14 7a5 5 0 0 0-5 5c0 4 5 9 5 9s5-5 5-9a5 5 0 0 0-5-5z" fill="var(--white)"/><circle cx="14" cy="12" r="2" fill="var(--blue-deep)"/></svg>
    <span>P.O. Box 4127<br>Harel Park, Israel 40512</span>
  </div>
  <div class="contact-row">
    <svg width="28" height="28" viewBox="0 0 28 28"><circle cx="14" cy="14" r="14" fill="var(--blue-deep)"/><path d="M10 8l3 3-2 2c1 2 2 3 4 4l2-2 3 3-2 2c-5 0-10-5-10-10z" fill="var(--white)"/></svg>
    <span style="padding-top:5px">+972-50-555-0182</span>
  </div>
  <div class="contact-row">
    <svg width="28" height="28" viewBox="0 0 28 28"><circle cx="14" cy="14" r="14" fill="var(--blue-deep)"/><rect x="7" y="9" width="14" height="10" fill="var(--white)"/><path d="M7 9l7 6 7-6" fill="none" stroke="var(--blue-deep)" stroke-width="1.3"/></svg>
    <span style="padding-top:5px">mail@klv.example</span>
  </div>
</div>

<div class="abs foot-line"></div>
<p class="abs copyright">Copyright © 2023 <u>KLV Messaging</u>. All Right Reserved</p>

</body>
</html>
```